iPhone iOS 7 App For Managing Tasks/Photos for Internal Company Use

We need an app design that displays company objectives and task, and provides the interface for employees to complete a task by uploading a photo and adding comments.

Please see attached mock up sketches as a rough guideline

Final delivery of files must contain PSD, and all layers/objects sliced both is PSD and PNG files

Target Market(s)

This is a tool for internal employee use

Industry/Entity Type

It Company

Requirements
Must have
• Must include logo, and match the colour scheme
Use iPhone iOS 7 Style

```html
<!DOCTYPE html>
<html lang="en">
<head>
<meta charset="utf-8">
<title>Objectives App Screens</title>
<link href="https://fonts.googleapis.com/css2?family=Heebo:wght@300;400;700&display=swap" rel="stylesheet">
<style>
  :root {
    --bg-top: #a9b1b1;
    --bg-bottom: #a3a8b5;
    --screen: #dcdbdb;
    --header: #d9d8d8;
    --rule: #c4c4c4;
    --teal: #4b6a6d;
    --teal-dark: #3c5659;
    --ink: #3b3b3b;
    --ink-soft: #5d6466;
    --field: #ecebeb;
    --tile: #e6e5e5;
    --icon: #eef2f2;
    --stamp: #e0452c;
  }
  * { box-sizing: border-box; margin: 0; padding: 0; }
  html, body { width: 1200px; height: 1000px; overflow: hidden; }
  body {
    position: relative;
    background: linear-gradient(180deg, var(--bg-top), var(--bg-bottom));
    font-family: "Heebo", "Helvetica Neue", Arial, sans-serif;
    font-weight: 300;
    color: var(--ink);
  }
  .screen {
    position: absolute;
    width: 376px;
    background: var(--screen);
    overflow: hidden;
    box-shadow: 0 18px 40px rgba(60,70,75,.25);
  }
  .screen--objective { left: 24px; top: 228px; height: 570px; }
  .screen--task { left: 418px; top: 193px; height: 569px; }
  .screen--news { left: 807px; top: 160px; height: 565px; }

  .nav-bar {
    height: 57px;
    background: var(--header);
    border-bottom: 1px solid var(--rule);
    position: relative;
    display: flex; align-items: center; justify-content: center;
  }
  .nav-title { font-size: 29px; color: #7b8284; font-weight: 300; }
  .nav-back {
    position: absolute; left: 12px; top: 50%; transform: translateY(-50%);
    display: flex; align-items: center; gap: 4px;
    color: var(--teal); font-size: 20px; font-weight: 400;
  }
  .nav-back svg { width: 14px; height: 24px; }

  .page-heading { text-align: center; font-size: 31px; margin-top: 14px; color: var(--ink); }

  .task-list { list-style: none; margin: 16px 14px 0; }
  .task-row {
    height: 51px; margin-bottom: 9px;
    border: 1px solid var(--rule); border-top: 4px solid var(--teal);
    position: relative;
    display: flex; align-items: center; justify-content: center;
    font-size: 24px; color: var(--ink);
  }
  .task-row--active { background: var(--teal); color: #2f4446; }
  .task-check { position: absolute; left: 16px; top: 50%; transform: translateY(-50%); width: 22px; height: 22px; }

  .photo-drop {
    width: 148px; height: 129px; margin: 22px auto 0;
    background: var(--tile); border: 1px solid #d0d0d0;
    display: flex; align-items: center; justify-content: center;
  }
  .comment-field {
    margin: 17px 37px 0 38px; height: 120px;
    background: var(--field); padding: 6px 11px;
    font-size: 15px; color: var(--ink-soft);
  }
  .primary-button {
    display: flex; align-items: center; justify-content: center;
    margin: 32px 37px 0 38px; height: 50px;
    background: var(--teal); color: #eef2f2;
    font-size: 21px; font-weight: 400;
    box-shadow: 0 2px 0 var(--teal-dark);
  }

  .segment { display: flex; margin: 19px 14px 0; height: 38px; }
  .segment-tab {
    flex: 1; display: flex; align-items: center; justify-content: center;
    font-size: 23px; color: var(--ink);
  }
  .segment-tab--on { border: 1px solid var(--ink-soft); border-top: 3px solid var(--teal); border-bottom: none; }
  .segment-tab--off { border-bottom: 1px solid var(--ink-soft); }

  .feed { margin: 14px 14px 0; }
  .feed-item { border-bottom: 1px solid var(--rule); padding-bottom: 4px; margin-bottom: 3px; }
  .feed-head { display: flex; justify-content: space-between; align-items: baseline; }
  .feed-author { font-size: 15px; color: var(--teal); font-weight: 400; }
  .feed-time { font-size: 9px; color: var(--stamp); font-weight: 400; }
  .feed-body { display: flex; gap: 7px; margin-top: 2px; }
  .feed-thumb { flex: 0 0 58px; height: 56px; margin-top: 2px; }
  .feed-text { font-size: 10px; line-height: 11.6px; color: #333; font-weight: 400; height: 70px; overflow: hidden; }

  .tab-bar {
    position: absolute; left: 0; right: 0; bottom: 0; height: 64px;
    background: var(--teal); display: flex;
  }
  .tab-item {
    flex: 1; display: flex; flex-direction: column; align-items: center; justify-content: flex-end;
    padding-bottom: 6px; color: var(--icon); font-size: 10px; font-weight: 400;
  }
  .tab-item--current { background: var(--teal-dark); }
  .tab-item svg { width: 40px; height: 38px; margin-bottom: 2px; }
</style>
</head>
<body>

<svg width="0" height="0" style="position:absolute">
  <defs>
    <symbol id="icon-home" viewBox="0 0 40 38"><path d="M4 20 L20 4 L36 20 M9 15 V35 H31 V15 M16 35 V24 H24 V35" fill="none" stroke="currentColor" stroke-width="1.6"/></symbol>
    <symbol id="icon-objectives" viewBox="0 0 40 38"><g fill="none" stroke="currentColor" stroke-width="1.6"><rect x="4" y="6" width="5" height="5"/><rect x="4" y="15" width="5" height="5"/><rect x="4" y="24" width="5" height="5"/><rect x="13" y="6" width="24" height="5"/><rect x="13" y="15" width="24" height="5"/><rect x="13" y="24" width="24" height="5"/><path d="M4 8 l2 2 l4 -5 M4 17 l2 2 l4 -5"/></g></symbol>
    <symbol id="icon-news" viewBox="0 0 40 38"><g fill="none" stroke="currentColor" stroke-width="1.6"><rect x="6" y="3" width="28" height="32"/><rect x="10" y="8" width="10" height="9"/><path d="M23 9h8M23 13h8M23 17h8M10 21h21M10 25h21M10 29h21"/></g></symbol>
    <symbol id="icon-logout" viewBox="0 0 40 38"><g fill="none" stroke="currentColor" stroke-width="1.6"><path d="M22 6 L34 15 L22 24 V19 C14 19 9 22 6 28 C7 19 12 12 22 11 Z"/><path d="M4 18 V34 H30 V27"/></g></symbol>
  </defs>
</svg>

<section class="screen screen--objective">
  <header class="nav-bar">
    <span class="nav-back"><svg viewBox="0 0 14 24"><path d="M12 2 L3 12 L12 22" fill="none" stroke="currentColor" stroke-width="3"/></svg>Back</span>
    <h1 class="nav-title">Objectives</h1>
  </header>
  <h2 class="page-heading">Objective #2</h2>
  <ul class="task-list">
    <li class="task-row"><svg class="task-check" viewBox="0 0 22 22"><rect x="2" y="4" width="16" height="16" fill="none" stroke="#4b6a6d" stroke-width="3"/><path d="M5 11 l4 4 l11 -14" fill="none" stroke="#4b6a6d" stroke-width="3"/></svg>Task #1</li>
    <li class="task-row task-row--active">Task #2</li>
    <li class="task-row"><svg class="task-check" viewBox="0 0 22 22"><rect x="3" y="3" width="16" height="16" fill="none" stroke="#4b6a6d" stroke-width="3"/></svg>Task #3</li>
    <li class="task-row"><svg class="task-check" viewBox="0 0 22 22"><rect x="3" y="3" width="16" height="16" fill="none" stroke="#4b6a6d" stroke-width="3"/></svg>Task #4</li>
  </ul>
  <nav class="tab-bar">
    <span class="tab-item"><svg><use href="#icon-home"/></svg>Home</span>
    <span class="tab-item tab-item--current"><svg><use href="#icon-objectives"/></svg>Objectives</span>
    <span class="tab-item"><svg><use href="#icon-news"/></svg>News</span>
    <span class="tab-item"><svg><use href="#icon-logout"/></svg>Logout</span>
  </nav>
</section>

<section class="screen screen--task">
  <header class="nav-bar">
    <span class="nav-back"><svg viewBox="0 0 14 24"><path d="M12 2 L3 12 L12 22" fill="none" stroke="currentColor" stroke-width="3"/></svg>Back</span>
    <h1 class="nav-title">Objectives</h1>
  </header>
  <h2 class="page-heading">Task #2</h2>
  <div class="photo-drop">
    <svg width="128" height="96" viewBox="0 0 128 96" fill="none" stroke="#4b6a6d" stroke-width="3">
      <path d="M4 24 H26 L34 12 H66 L74 24 H102 V62 M84 86 H4 Z"/>
      <circle cx="52" cy="50" r="23"/>
      <path d="M88 32 h8"/>
      <circle cx="102" cy="74" r="21" fill="#e6e5e5"/>
      <path d="M102 62 V86 M90 74 H114"/>
    </svg>
  </div>
  <div class="comment-field">Comments</div>
  <span class="primary-button">Save &amp; Complete</span>
  <nav class="tab-bar">
    <span class="tab-item"><svg><use href="#icon-home"/></svg>Home</span>
    <span class="tab-item tab-item--current"><svg><use href="#icon-objectives"/></svg>Objectives</span>
    <span class="tab-item"><svg><use href="#icon-news"/></svg>News</span>
    <span class="tab-item"><svg><use href="#icon-logout"/></svg>Logout</span>
  </nav>
</section>

<section class="screen screen--news">
  <header class="nav-bar"><h1 class="nav-title">News</h1></header>
  <div class="segment">
    <span class="segment-tab segment-tab--on">All News</span>
    <span class="segment-tab segment-tab--off">My News</span>
  </div>
  <div class="feed">
    <article class="feed-item">
      <div class="feed-head"><span class="feed-author">Martin Hale</span><span class="feed-time">5 mins ago</span></div>
      <div class="feed-body"><div class="feed-thumb" role="img" aria-label="Photo of an office interior" style="background:linear-gradient(135deg,#6b4a33,#a7876a)"></div>
      <p class="feed-text">Lorem ipsum dolor sit amet, consectetur adipisicing elit, sed do eiusmod tempor incididunt ut labore et dolore magna aliqua. Ut enim ad minim veniam, quis nostrud exercitation ullamco laboris nisi ut aliquip ex ea commodo consequat. Duis aute irure dolor in reprehenderit in voluptate velit esse cillum dolore eu fugiat nulla</p></div>
    </article>
    <article class="feed-item">
      <div class="feed-head"><span class="feed-author">Me</span><span class="feed-time">2 hours ago</span></div>
      <div class="feed-body"><div class="feed-thumb" role="img" aria-label="Screenshot of a web page" style="background:linear-gradient(180deg,#3a3f48 45%,#d9603a 45%,#e8e8e8)"></div>
      <p class="feed-text">Lorem ipsum dolor sit amet, consectetur adipisicing elit, sed do eiusmod tempor incididunt ut labore et dolore magna aliqua. Ut enim ad minim veniam, quis nostrud exercitation ullamco laboris nisi ut aliquip ex ea commodo consequat. Duis aute irure dolor in reprehenderit in voluptate velit esse cillum dolore eu fugiat nulla</p></div>
    </article>
    <article class="feed-item">
      <div class="feed-head"><span class="feed-author">Sam Porter</span><span class="feed-time">2:15 pm November 22 2013</span></div>
      <div class="feed-body"><div class="feed-thumb" role="img" aria-label="Photo of a dark device" style="background:linear-gradient(90deg,#2c2c2c 70%,#f2f2f2 70%)"></div>
      <p class="feed-text">Lorem ipsum dolor sit amet, consectetur adipisicing elit, sed do eiusmod tempor incididunt ut labore et dolore magna aliqua. Ut enim ad minim veniam, quis nostrud exercitation ullamco laboris nisi ut aliquip ex ea commodo consequat. Duis aute irure dolor in reprehenderit in voluptate velit esse cillum dolore eu fugiat nulla</p></div>
    </article>
    <article class="feed-item">
      <div class="feed-head"><span class="feed-author">Leo Barton</span><span class="feed-time">11:37 am November 22 2013</span></div>
      <div class="feed-body"><div class="feed-thumb" role="img" aria-label="Colourful illustration" style="background:linear-gradient(135deg,#e0674f,#b23d6b 60%,#3f8f9a)"></div>
      <p class="feed-text">Lorem ipsum dolor sit amet, consectetur adipisicing elit, sed do eiusmod tempor incididunt ut labore et dolore magna aliqua. Ut enim ad minim veniam, quis nostrud exercitation ullamco laboris nisi ut aliquip ex ea commodo consequat. Duis aute irure dolor in reprehenderit in voluptate velit esse cillum dolore eu fugiat nulla</p></div>
    </article>
    <article class="feed-item">
      <div class="feed-head"><span class="feed-author">Me</span><span class="feed-time">9:47 am November 22 2013</span></div>
      <div class="feed-body"><div class="feed-thumb" role="img" aria-label="Photo thumbnail" style="background:#3a3a3a"></div>
      <p class="feed-text">Lorem ipsum dolor sit amet, consectetur adipisicing elit, sed do eiusmod tempor incididunt ut labore et dolore magna aliqua.</p></div>
    </article>
  </div>
  <nav class="tab-bar">
    <span class="tab-item"><svg><use href="#icon-home"/></svg>Home</span>
    <span class="tab-item"><svg><use href="#icon-objectives"/></svg>Objectives</span>
    <span class="tab-item tab-item--current"><svg><use href="#icon-news"/></svg>News</span>
    <span class="tab-item"><svg><use href="#icon-logout"/></svg>Logout</span>
  </nav>
</section>

</body>
</html>
```